Wanted: amazing Flyer for professional Photovoltaik-Installations
target-audience
With 'brightmere.energy' in Austria we want to build a brand for high quality and professional photovoltaic installations. The target group are homeowners or end users but also commercial customers.
Therefore we are working with a network of electrical installers. The flyer is intended for distribution to households and to stimulate interest and curiosity for the subject and ultimately to animate, to make an appointment at a consulting center in the region. 1/3 of the contents of the flyer should contain individual information on each partner company.
Description
Design a leporello in A4 (2 times folded) for the brand brightmere.energy which transports the theme and the brand emotionally and reflects the three main arguments:
1. reduce your power bill (economically, it is worth)
2. Independence (from the energy supplier)
3. Clean energy (contribution to ENVIRONMENTAL PROTECTION, CO2 reduction ...)
Eventually you can support the main arguments with infographics.
Style: high quality, professional, modern.
Fundamental for the design: existing logo (see Appendix)
Please refer to the press release in the appendix (not let yourself be confused by the name parcels and plenty, this has something to do with the history of the company and has no meaning at all to the consumers. Here is brightmere.energy the only form of communication).
If you have questions do not hesitate to contact us.

```html
<!DOCTYPE html>
<html lang="de">
<head>
<meta charset="utf-8">
<title>brightmere.energy – Leporello</title>
<link href="https://fonts.googleapis.com/css2?family=Roboto:wght@300;400;500;700&family=Roboto+Condensed:wght@400;700&display=swap" rel="stylesheet">
<style>
:root{
  --yellow:#f7b500;
  --orange:#f39200;
  --grey:#636363;
  --grey-dark:#555;
  --green:#8dc21f;
  --blue:#1ea7e1;
  --navy:#2b3a8c;
  --white:#fff;
  --ink:#333;
  --sky-top:#3d7fd6;
  --sky-mid:#9cc6ef;
  --page:#eef0f2;
}
*{box-sizing:border-box;margin:0;padding:0}
html,body{width:800px;height:1200px;overflow:hidden;background:var(--page);font-family:"Roboto",Arial,sans-serif;color:var(--ink)}
.spread{position:absolute;left:20px;width:760px;background:var(--white);overflow:hidden;box-shadow:0 6px 14px rgba(0,0,0,.18)}
.spread--outside{top:20px;height:540px}
.spread--inside{top:596px;height:584px}
.abs{position:absolute}

/* outside spread */
.sky{left:0;top:0;width:520px;height:540px;background:radial-gradient(circle at 130px 150px,#fff 0,#fff 28px,rgba(255,255,255,.7) 60px,rgba(255,255,255,0) 140px),linear-gradient(180deg,var(--sky-top) 0%,var(--sky-mid) 55%,#2d5fb0 80%,#1d3f80 100%)}
.tab-heading{left:253px;top:20px;width:245px;height:48px;background:var(--yellow);clip-path:polygon(0 0,100% 0,88% 100%,0 100%);color:var(--white);font-size:13px;letter-spacing:1px;text-transform:uppercase;padding:8px 12px;line-height:1.35}
.text-block{background:var(--grey);color:var(--white)}
.how-text{left:253px;top:68px;width:245px;height:282px;font-size:9.3px;line-height:1.28;padding:10px 12px}
.how-text p{margin-bottom:2px}
.slogan-band{left:30px;top:345px;width:500px;height:80px;background:var(--yellow);clip-path:polygon(0 0,100% 0,100% 100%,14% 100%);color:var(--white);font-weight:300;font-size:21px;line-height:1.25;padding:14px 0 0 110px}
.contact-box{left:290px;top:425px;width:230px;height:115px;font-weight:700;font-size:10.5px;line-height:1.4;padding:14px 12px}
.brand-panel{left:520px;top:0;width:240px;height:540px;background:linear-gradient(180deg,#fff 0,#fff 28%,#c5dcf4 40%,#6da2df 65%,#2b5aa8 100%)}
.brand{left:20px;top:70px;display:flex;align-items:center;gap:10px;font-size:23px;font-weight:400;color:var(--ink)}
.brand-dot{width:22px;height:22px;border-radius:50%;background:var(--orange)}
.benefit{left:20px;width:220px;height:58px;display:flex;align-items:center}
.benefit-icon{width:56px;height:56px;border-radius:50%;flex:none;display:flex;align-items:center;justify-content:center;position:relative;z-index:1}
.benefit-label{background:rgba(255,255,255,.85);margin-left:-10px;padding:6px 8px 6px 18px;font-size:12px;line-height:1.25;width:175px}
.benefit--cost{top:175px}.benefit--cost .benefit-icon{background:var(--blue)}.benefit--cost .benefit-label{color:var(--blue)}
.benefit--free{top:265px}.benefit--free .benefit-icon{background:var(--orange)}.benefit--free .benefit-label{color:var(--orange)}
.benefit--green{top:355px}.benefit--green .benefit-icon{background:var(--green)}.benefit--green .benefit-label{color:var(--green)}

/* inside spread */
.why-heading{left:0;top:16px;width:245px;height:44px;background:var(--yellow);clip-path:polygon(0 0,100% 0,90% 100%,0 100%);color:var(--white);font-size:18px;padding:10px 12px}
.why-sub{left:20px;top:70px;width:220px;text-align:center;color:var(--orange);font-size:14px;line-height:1.25}
.why-text{left:16px;top:118px;width:225px;font-size:9.6px;line-height:1.32;color:var(--ink)}
.partner-card{left:16px;top:258px;width:230px;height:80px;display:flex;background:var(--grey-dark)}
.partner-photo{width:70px;height:80px;background:linear-gradient(180deg,#f1e7d8,#d8c5a8);border:2px solid #fff}
.partner-name{color:var(--white);font-size:10px;line-height:1.55;padding:14px 8px;letter-spacing:.4px;text-transform:uppercase}
.partner-name b{color:var(--yellow)}
.install-photo{left:0;top:345px;width:253px;height:220px;background:linear-gradient(180deg,#7fb6ea 0%,#cfe2f5 35%,#3c67b8 60%,#1e3a7a 100%)}
.section-heading{color:var(--white);font-size:15px;line-height:1.2;padding:7px 12px;clip-path:polygon(0 0,100% 0,88% 100%,0 100%)}
.head--green{left:253px;top:16px;width:240px;height:50px;background:var(--green)}
.head--blue{left:253px;top:306px;width:225px;height:46px;background:var(--blue)}
.indep-text{left:253px;top:66px;width:240px;height:160px;font-size:10.4px;line-height:1.32;padding:10px 12px}
.climate-text{left:253px;top:352px;width:225px;height:215px;font-size:10.4px;line-height:1.32;padding:10px 12px}
.team-photo{left:493px;top:0;width:267px;height:567px;background:linear-gradient(180deg,#e4e4e4,#b9b9b9 70%,#9e9e9e)}
.offer-band{left:253px;top:226px;width:485px;height:80px;background:var(--yellow);clip-path:polygon(0 0,100% 0,88% 100%,0 100%);color:var(--white);padding:8px 12px}
.offer-band .claim{font-family:"Roboto Condensed",Arial,sans-serif;font-weight:700;font-size:18px}
.offer-band .welcome{font-weight:300;font-size:25px;line-height:1.3}
.offer-band .welcome b{font-weight:700}
.appointment-box{left:528px;top:330px;width:210px;height:210px;background:linear-gradient(180deg,#a5d233,var(--green));border-radius:16px;border:2px solid #fff;color:var(--white);font-size:8px;line-height:1.35;text-align:center;padding:16px 10px}
.appointment-box .gap{margin-top:16px}
.appointment-box .url{font-size:10px;font-weight:500;margin-top:4px}
.bottom-strip{left:0;top:567px;width:760px;height:17px;background:var(--yellow)}
</style>
</head>
<body>

<section class="spread spread--outside">
  <div class="abs sky" role="img" aria-label="Foto: blauer Himmel mit strahlender Sonne über Solarmodulen"></div>
  <h2 class="abs tab-heading">Wie funktioniert<br>eine PV-Anlage?</h2>
  <div class="abs text-block how-text">
    <p>Photovoltaikmodule – oft auf dem Gebäudedach installiert – verwandeln Sonnenlicht in Gleichstrom. Dieser wird über einen so genannten Wechselrichter in Wechselstrom umgewandelt und in das Hausnetz eingespeist.</p>
    <p>Alles, was Sie selbst verbrauchen, kostet Sie keinen Cent, verbrauchen Sie mehr, als die Anlage liefert, beziehen Sie weiterhin Strom von Ihrem Energieversorger. Verbrauchen Sie weniger, wird der Überschuss von Ihrem Energieversorger gekauft und von Ihrer Stromrechnung abgezogen.</p>
    <p>Alternativ können Sie Überschüsse auch in einem Energiespeicher sammeln und verbrauchen, wenn keine Sonne scheint. Um das Optimum aus Ihrer PV-Anlage herauszuholen, ist die Größenordnung im Zusammenhang mit Ihren Gebrauchsgewohnheiten sehr wichtig.</p>
  </div>
  <div class="abs slogan-band">Entfesseln sie die<br>Kraft Der Sonne</div>
  <div class="abs text-block contact-box">Vereinbaren Sie am besten gleich jetzt einen Termin in unserem Beratungszentrum und wir finden für Sie unverbindlich die ideale Lösung:<br>0660 000 00 00 – Herr Lindner</div>

  <div class="abs brand-panel" role="img" aria-label="Foto: Himmel über Solarmodulen">
    <div class="abs brand"><span class="brand-dot"></span>brightmere.energy</div>
    <div class="abs benefit benefit--cost">
      <div class="benefit-icon"><svg width="26" height="30" viewBox="0 0 26 30"><rect x="6" y="0" width="4" height="9" fill="#fff"/><rect x="16" y="0" width="4" height="9" fill="#fff"/><path d="M2 9h22v8a9 9 0 0 1-9 9h-4a9 9 0 0 1-9-9z" fill="#fff"/><rect x="11" y="25" width="4" height="5" fill="#fff"/></svg></div>
      <div class="benefit-label">Reduzieren Sie ihre<br><b>Stromkosten</b></div>
    </div>
    <div class="abs benefit benefit--free">
      <div class="benefit-icon"><svg width="28" height="28" viewBox="0 0 28 28"><rect width="28" height="28" fill="var(--navy)"/><path d="M7 0v28M14 0v28M21 0v28M0 7h28M0 14h28M0 21h28" stroke="#7d8fd6" stroke-width="1"/></svg></div>
      <div class="benefit-label">Werden Sie unabhängig<br>von ihrem <b>Energieversorger</b></div>
    </div>
    <div class="abs benefit benefit--green">
      <div class="benefit-icon"><svg width="28" height="28" viewBox="0 0 28 28"><path d="M4 24C4 10 14 4 26 3c-1 12-8 21-22 21z" fill="#fff"/><path d="M4 24L20 9" stroke="var(--green)" stroke-width="1.5"/></svg></div>
      <div class="benefit-label">Leisten sie einen Wertfollen<br><b>Beitrag zum Klimaschutz</b></div>
    </div>
  </div>
</section>

<section class="spread spread--inside">
  <h2 class="abs why-heading">Warum eine <b>PV-Anlage?</b></h2>
  <h3 class="abs why-sub">Schmelzende Kosten statt<br><b>geschmalzener Preise</b></h3>
  <p class="abs why-text">In Ihre neue Photovoltaik-Anlage zu investieren, rechnet sich: Schon nach wenigen Jahren haben Sie die Anschaffungskosten durch die viel geringeren Stromkosten wieder eingespart. Ab diesem Zeitpunkt verdient Ihre Anlage für Sie Geld – und das über eine Gesamt-Betriebsdauer von gut 25 Jahren. Kommen Sie in unser Beratungszentrum und wir rechnen es Ihnen vor!</p>
  <div class="abs partner-card">
    <div class="partner-photo" role="img" aria-label="Porträtfoto einer Ansprechpartnerin"></div>
    <div class="partner-name">Elektro Beispielbetrieb<br><b>Ihr PV-Profi</b> aus<br>der Nachbarschaft</div>
  </div>
  <div class="abs install-photo" role="img" aria-label="Foto: Monteure installieren Solarmodule auf einem Dach"></div>

  <div class="abs team-photo" role="img" aria-label="Foto: Beraterin und Berater mit verschränkten Armen"></div>
  <h2 class="abs section-heading head--green">Unabhängig vom<br>Energieversorger</h2>
  <p class="abs text-block indep-text">Ihre neue Photovoltaik-Anlage macht Sie auch unabhängig von Ihrem Energieversorger. Steigende Strompreise lassen Sie in Zukunft kalt. Und wenn Sie sich zusätzlich für eine moderne Energiespeicherlösung entscheiden, sitzen Sie beim nächsten Stromausfall nicht im Dunkeln.</p>
  <div class="abs offer-band">
    <div class="claim">leistbar investieren lange profitieren!</div>
    <div class="welcome">Wir freuen uns <b>auf Sie!</b></div>
  </div>
  <h2 class="abs section-heading head--blue">Ihr Beitrag zum<br>Klimaschutz</h2>
  <p class="abs text-block climate-text">Unsere Generation hat es in der Hand, den Klimawandel zu verhindern. Mit Ihrer neuen Photovoltaik-Anlage produzieren Sie reinen grünen Strom, reduzieren damit die Treibhausgasbelastung unseres Planeten und leisten so einen wertvollen Beitrag zur Schonung der Umwelt.</p>
  <div class="abs appointment-box">
    <p>Kommen Sie in unser Beratungszentrum und erfahren Sie, wie die Gratis-Energie der Sonne in Zukunft auch für Sie arbeiten kann! Vereinbaren Sie gleich einen</p>
    <p class="gap">Beratungstermin:<br>0660 000 00 00<br>Herr Lindner<br>lindner@brightmere.energy</p>
    <p class="url">www.brightmere.energy/partner1</p>
  </div>
  <div class="abs bottom-strip"></div>
</section>

</body>
</html>
```